Web Design Project

Website Design Brief

Company Details
1a) Name of Company

BRAMBLECOURT
1) What is the nature of your business?: Briefly describe your products or services:

INDEPENDENT CONTEMPORARY TRADITIONAL ITALIAN RESTAURANT IN THE HEART OF FENWORTH QUAY ALSO CATERING FOR PRIVATE CORPORATE EVENTS AND WEDDING RECEPTIONS

1a) Who is your target market? Who are you hoping to reach with your site?

CITY CORPORATES, LOCAL CORPORATES/BUSINESSES, LOCAL RESIDENTS, VISITORS TO THE DOCK, LOCAL HOTELS

Website Details
1b) Do you have an existing website? If so, what is the URL?
HTTP://WWW.BRAMBLECOURTFOODHALL.COM

2b) IMPORTANT: Please list at least 3 URLs (web addresses) of high quality sites that you like the look of (these do not have to be sites who’s business is similar to yours. It aids us in determining what your design style is.) Please consider layout, colours, navigation, graphics, and typography.

http://www.thewexmoor.co.uk/

http://www.corriveth.co.uk/

http://www.tovirestaurant.com/

http://www.osprelo.co.uk/

3b) What colours or colour schemes would you like?

WHITE, BLACK, SILVER/ALUMINIUM (PLS LOOK AT OUR OUTSIDE CHAIRS)

4b) List the Navigation links for your Site:

5b) What type of look are you trying to achieve? (e.g. clean, high-tech, conservative, warm, flashy, etc.)

SIMPLE ELEGANT CLASSY INFORMATIVE, EASY TO USE, A REFLECTION OF THE BUSINESS ITSELF

6b) Please provide the addresses of competitors' sites, if possible:

Do not contact the client direct - all questions should go through Larkmoor Hospitality - info@larkmoorhospitality.co.uk
Updates

thanks for the designs that I have received so far. I have these general comments:

- please avoid using icons for phones or paperclips etc 
- use dummy text (one design used text from another website) 
- there won't any live social media feeds to the site
the client likes a lot of the designs that this company comes up with: 

i look forward to see some more designs

hi all, 

further to my last update, here are a few more pointers:
- there will be no search facilities - so no "search" box please 
- please just use the images supplied - no stock ones
- use just the page names give (no other pages) 

The client is looking for a simple, elegant design. 

Many thanks 
Neil 

thanks for all the designs. 

I have uploaded another file to the brief which shows some posters that the client particularly likes. Perhaps the homepage could consist of large rectangle made up of a number of boxes - for some introductory text, a large image, mailing list, contact details, Lunch Special etc - just an idea! 
It's clear that the client likes clean lines with square edges. 
I want to be able to pass the designs directly onto the client so can designers avoid adding extra info or page. For example one design has a tab for a "Gift Card" - it will be easier for me if such additions are avoided. 

thanks!                                                                                                                                                                                                                                                                                                                                                                                                    

Thank you for all your designs - please keep them coming! 

hi all,

I am meeting the client tomorrow afternoon so please submit revisions / designs before then. 

Many thanks, 
Neil

Target Market(s)

Business people, upmarket etc

Industry/Entity Type

Business

Requirements
Must have
• - The home page needs a slide show of images as well as:
- a mailing list form - very simple, "Join our mailing list - name, email"
- 3 or 4 sentences of text
- facebook link

```html
<!DOCTYPE html>
<html lang="en">
<head>
<meta charset="utf-8">
<title>Bramblecourt Italian — Welcome</title>
<link rel="stylesheet" href="https://fonts.googleapis.com/css2?family=Open+Sans:wght@400;600&family=Arvo:wght@700&display=swap">
<style>
  :root {
    --header-top: #3f444b;
    --header-mid: #8a8e94;
    --nav-bg: #4a4f56;
    --nav-dark: #3a3e44;
    --nav-text: #9ea3a9;
    --nav-active: #ffffff;
    --stage-bg: #f3f3f3;
    --stage-edge: #e2e2e2;
    --frame: #ffffff;
    --footer-bg: #50555c;
    --footer-text: #7d828a;
    --caption-bg: rgba(40, 40, 40, 0.72);
    --dot: #e4e2dc;
    --dot-active: #5f6770;
    --input-bg: #8b9097;
  }
  * { box-sizing: border-box; margin: 0; padding: 0; }
  html, body { width: 1200px; height: 812px; overflow: hidden; }
  body { position: relative; background: var(--stage-bg); font-family: "Open Sans", Arial, sans-serif; }

  .site-header {
    position: absolute; left: 0; top: 0; width: 1200px; height: 131px;
    background: radial-gradient(ellipse 520px 180px at 600px 70px, var(--header-mid), var(--header-top) 100%);
    border-bottom: 1px solid #2e3237;
  }
  .brand { position: absolute; left: 0; width: 1200px; top: 20px; text-align: center; color: #fff; font-weight: 400; }
  .brand-name { display: block; font-size: 46px; letter-spacing: 3px; line-height: 58px; }
  .brand-sub { display: block; font-size: 16px; letter-spacing: 5px; line-height: 20px; }

  .main-nav {
    position: absolute; left: 0; top: 140px; width: 1200px; height: 44px;
    background: linear-gradient(var(--nav-bg), var(--nav-dark));
    box-shadow: 0 -6px 8px rgba(0,0,0,0.25);
  }
  .main-nav ul { list-style: none; }
  .main-nav li {
    position: absolute; top: 12px; font-size: 15px; letter-spacing: 1.5px;
    color: var(--nav-text); text-transform: uppercase;
  }
  .main-nav li.is-active { color: var(--nav-active); font-weight: 600; }

  .stage {
    position: absolute; left: 0; top: 184px; width: 1200px; height: 581px;
    background: linear-gradient(var(--stage-bg) 70%, var(--stage-edge));
  }
  .slide { position: absolute; background: var(--frame); padding: 3px; box-shadow: 0 2px 10px rgba(0,0,0,0.3); }
  .slide-photo { width: 100%; height: 100%; }
  .slide--left { left: 47px; top: 78px; width: 228px; height: 418px; }
  .slide--left .slide-photo { background: linear-gradient(120deg, #3a3a3a, #e8e6e2 40%, #c58a4a 60%, #f0efec); }
  .slide--right { left: 927px; top: 78px; width: 226px; height: 413px; }
  .slide--right .slide-photo { background: linear-gradient(200deg, #5a4a3a, #d8d4cc 35%, #9a5a50 60%, #1e1e1e); }
  .slide--center { left: 273px; top: 53px; width: 656px; height: 478px; z-index: 2; }
  .slide--center .slide-photo {
    position: relative;
    background: radial-gradient(ellipse 300px 200px at 300px 230px, #6b5130, #1e1b17 70%), #181614;
  }
  .caption {
    position: absolute; left: 312px; top: 284px; width: 338px; height: 174px;
    background: var(--caption-bg); color: #fff; padding: 16px 12px;
  }
  .caption h1 { font-family: "Arvo", Georgia, serif; font-size: 19px; line-height: 23px; letter-spacing: 0.5px; }
  .caption .lead { margin-top: 8px; font-size: 10px; line-height: 12px; letter-spacing: 0.6px; }
  .caption .note { margin-top: 8px; font-size: 6px; line-height: 8px; letter-spacing: 0.3px; color: #ddd; }

  .slide-dots { position: absolute; left: 544px; top: 545px; display: flex; gap: 4px; }
  .slide-dots span {
    width: 19px; height: 19px; border-radius: 50%;
    background: linear-gradient(#f3f2ee, var(--dot)); box-shadow: 0 1px 2px rgba(0,0,0,0.35);
  }
  .slide-dots span.is-current { background: var(--dot-active); }

  .site-footer {
    position: absolute; left: 0; top: 765px; width: 1200px; height: 47px;
    background: linear-gradient(#5a5f66, var(--footer-bg));
  }
  .address { position: absolute; left: 0; width: 1200px; top: 11px; text-align: center; color: var(--footer-text); font-size: 10px; letter-spacing: 2.5px; text-transform: uppercase; }
  .legal { position: absolute; left: 0; width: 1200px; top: 29px; text-align: center; color: #6c7178; font-size: 4.5px; letter-spacing: 1px; text-transform: uppercase; }
  .social { position: absolute; left: 967px; top: 13px; display: flex; gap: 3px; }
  .social span { width: 19px; height: 19px; background: #1c1c1c; border: 1px solid #8a8e94; }
  .mailing { position: absolute; left: 1059px; top: 6px; width: 136px; color: #fff; }
  .mailing h2 { font-size: 6px; letter-spacing: 1px; font-weight: 600; }
  .mailing .field { display: block; height: 8px; margin-top: 3px; width: 96px; background: var(--input-bg); color: #333; font-size: 4px; line-height: 8px; padding-left: 2px; }
  .mailing .submit { position: absolute; left: 98px; top: 25px; width: 38px; height: 8px; background: #3a3e44; color: #ccc; font-size: 4px; line-height: 8px; text-align: center; }
</style>
</head>
<body>
  <header class="site-header">
    <div class="brand">
      <span class="brand-name">BRAMBLECOURT</span>
      <span class="brand-sub">ITALIAN</span>
    </div>
  </header>

  <nav class="main-nav">
    <ul>
      <li class="is-active" style="left:174px">Welcome</li>
      <li style="left:307px">Restaurant</li>
      <li style="left:464px">Menu</li>
      <li style="left:558px">Gallery</li>
      <li style="left:679px">Events</li>
      <li style="left:795px">Reservations</li>
      <li style="left:965px">Contact</li>
    </ul>
  </nav>

  <main class="stage">
    <div class="slide slide--left"><div class="slide-photo" role="img" aria-label="Plated grilled fish with salad and berry garnish"></div></div>
    <div class="slide slide--right"><div class="slide-photo" role="img" aria-label="Seared tuna steak on a white plate with bread basket behind"></div></div>
    <div class="slide slide--center">
      <div class="slide-photo" role="img" aria-label="The restaurant building lit up at night on the quayside">
        <div class="caption">
          <h1>Welcome to<br>The Bramblecourt Italian</h1>
          <p class="lead">Contemporary yacht style interior with unrivalled panoramic views of Fenworth Quay and the Alder Bridge.</p>
          <p class="note">The Bramblecourt Italian is located on the first floor of the historic Fenworth Quay Yacht Club.</p>
        </div>
      </div>
    </div>
    <div class="slide-dots"><span></span><span></span><span class="is-current"></span><span></span><span></span></div>
  </main>

  <footer class="site-footer">
    <p class="address">14 Fenworth Quay Row, City of London, EC9 4QZ.</p>
    <p class="legal">Privacy policy · Copyright © 2012 The Bramblecourt Italian. All rights reserved</p>
    <div class="social" aria-label="Social links"><span></span><span></span><span></span><span></span></div>
    <form class="mailing">
      <h2>JOIN OUR MAILING LIST</h2>
      <span class="field">NAME</span>
      <span class="field">EMAIL</span>
      <span class="submit">SUBMIT</span>
    </form>
  </footer>
</body>
</html>
```